Kitchen and bathroom exhaust fan cleaning business card design

A new business cleaning domestic - not commercial - exhaust/extractor fans in kitchens, bathrooms and en suites and kitchen range hood filters.

We would like a bright colour suggesting cleanliness (such a syellow or light green?)

I would like to see on the card preferably on the reverse:

"We clean kitchen and bathroom exhaust fans & Volrex Brightos
and
clean and repair range hood filters and replace carbon filters

We give Pensioner discounts
Updates

Designers pls note the TM in the contact filed after Pureflow Vents should be superscript as in the trademark sign. On the reverse of the card, I would like:: "We clean kitchen and bathroom exhaust fans & Volrex Brightos & clean and repair range hood filters and replace carbon filters We give Pensioner discounts

Reason: I will be out of the country for several days

Target Market(s)

people who are too lazy or too busy to clean their fan units and pensioners and others who are unable to do it.

Industry/Entity Type

Business

Contact Information for Business Card

ACT Clean FansTM Designer pls note the TM should be superscript as in the trademark sign
Neil Oakley
Mob: 0431 572 864
Email: pureflowvents@zentromail.com
PO Box 7152, Pellow ACT 2608

Requirements
Must have
• Designer pls note the TM in the contact filed after Pureflow Vents should be superscript as in the trademark sign.

On the reverse

and

```html
<!DOCTYPE html>
<html lang="en">
<head>
<meta charset="utf-8">
<title>Pureflow Vents – Business Card</title>
<link href="https://fonts.googleapis.com/css2?family=Fira+Sans+Condensed:ital,wght@0,400;0,800;1,500&family=Crimson+Text&display=swap" rel="stylesheet">
<style>
  :root {
    --page: #e6e6e6;
    --card-black: #1e1c1d;
    --accent-yellow: #e4ec3a;
    --brand-green: #1f8a41;
    --text-green: #2f8a44;
    --grille-light: #a9a9a9;
    --grille-dark: #6f6f6f;
    --band-edge: #efe3c6;
    --panel: #cfcfcf;
    --ink: #1a1a1a;
  }
  * { box-sizing: border-box; margin: 0; padding: 0; }
  html, body { width: 1200px; height: 900px; overflow: hidden; }
  body {
    background: var(--page);
    display: flex; flex-direction: column; align-items: center; justify-content: center;
    gap: 40px;
    font-family: "Fira Sans Condensed", sans-serif;
  }
  .card {
    width: 640px; height: 366px; position: relative; overflow: hidden;
    box-shadow: 0 6px 18px rgba(0,0,0,.25);
  }

  /* Contact side */
  .card--contact { background: var(--card-black); }
  .card--contact .band {
    position: absolute; left: 0; right: 0; height: 22px; background: var(--accent-yellow);
  }
  .band--top { top: 0; }
  .band--bottom { bottom: 0; }
  .contact-title {
    position: absolute; top: 78px; width: 100%; text-align: center;
    color: var(--text-green); font-style: italic; font-weight: 500; font-size: 30px; letter-spacing: -0.5px;
  }
  .contact-title sup { font-size: 15px; }
  .title-rule {
    position: absolute; top: 130px; left: 170px; width: 300px; height: 3px; background: var(--accent-yellow);
  }
  .contact-list {
    position: absolute; top: 178px; width: 100%; list-style: none; text-align: center;
    color: var(--text-green); font-size: 15px; line-height: 24px;
  }

  /* Brand side */
  .card--brand { background: var(--grille-light); }
  .grille {
    position: absolute; inset: 0;
    background: linear-gradient(180deg, var(--grille-light), var(--grille-dark) 50%, var(--grille-light));
  }
  .green-block {
    position: absolute; width: 70px; height: 110px; background: var(--brand-green);
  }
  .green-block--left { left: 0; top: 80px; border-right: 5px solid var(--band-edge); }
  .green-block--right { right: 0; bottom: 40px; border-left: 5px solid var(--band-edge); }
  .brand-name {
    position: absolute; top: 120px; width: 100%; text-align: center;
    color: var(--brand-green); font-weight: 800; font-size: 64px; letter-spacing: -1px;
  }
  .name-panel {
    position: absolute; top: 215px; left: 210px; width: 220px; height: 56px;
    background: var(--panel); border-radius: 8px;
    display: flex; align-items: center; justify-content: center;
    font-family: "Crimson Text", serif; font-size: 26px; color: var(--ink);
  }
</style>
</head>
<body>
  <section class="card card--contact">
    <div class="band band--top"></div>
    <h1 class="contact-title">Pureflow Vents<sup>TM</sup> Neil Oakley</h1>
    <div class="title-rule"></div>
    <ul class="contact-list">
      <li>0431 572 864</li>
      <li>pureflowvents@zentromail.com</li>
      <li>PO Box 7152, Pellow ACT 2608</li>
    </ul>
    <div class="band band--bottom"></div>
  </section>

  <section class="card card--brand">
    <div class="grille" role="img" aria-label="Perforated metal vent grille texture"></div>
    <div class="green-block green-block--left"></div>
    <div class="green-block green-block--right"></div>
    <h2 class="brand-name">Pureflow Vents</h2>
    <p class="name-panel">Neil Oakley</p>
  </section>
</body>
</html>
```